Skincare,Bodycare and haircare brochure

Please design a A4 3 fold brochure for Vexmira Pty Ltd. You may go to our website www.vexmira.example to understand what we do - certified organic skincare.
Content:

About Us: Our Mission
Vexmira’s mission is to make premium skin care products using only certified organic ingredients for a safer, purer world.

How are we diferent?
Vexmira specialises in the research and development of certified organic skin, hair and personal care products for everyone. We hold Certified Organic Licenses with the Verdant Tally Board who accredits our system with the Federal Harvest Purity Code of Australia and other international organic certification standards. Vexmira’s passion is to produce and deliver premium, safe and effective certified organic products to all of our customers.

Other headings: Skincare, Body Care, Hair Care, Essential Oils (leave room for us to put product pictures and product info (you can copy 3 products from each category from our website for draft),

Please provide a heading about our memberships: Please also see our website for info.

Then have a contact us section (doesn't have to be a page) It can even be on the front page.

Please also use the Attached logos. Please use vexmira logo with underline (company logo) and dunbrook crafted and Certified Organic logos.

Many deaigns dont allow me to put alotnof product infronation on it. please allow me to donsoMan

```html
<!DOCTYPE html>
<html lang="en">
<head>
<meta charset="utf-8">
<title>Vexmira – Tri-fold Brochure</title>
<link rel="stylesheet" href="https://fonts.googleapis.com/css2?family=Yesteryear&family=Montserrat:wght@600&family=PT+Sans+Narrow:wght@400;700&family=Libre+Baskerville&display=swap">
<style>
  :root {
    --cream: #fdf6f2;
    --brown: #6e2f12;
    --heading: #6b2c10;
    --title: #7a3414;
    --body: #3a2c26;
    --logo-tone: #c8aca4;
    --white: #ffffff;
    --pearl-light: #fbf2ee;
    --pearl-dark: #c9aaa0;
  }
  * { box-sizing: border-box; margin: 0; padding: 0; }
  html, body { width: 1200px; height: 849px; overflow: hidden; background: var(--cream); }
  .brochure { position: relative; width: 1200px; height: 849px; background: var(--cream); overflow: hidden; font-family: "PT Sans Narrow", sans-serif; color: var(--body); }

  .fold { position: absolute; top: 0; bottom: 0; width: 0; border-left: 1px dashed #9a7a6a; z-index: 3; }
  .fold--one { left: 391px; }
  .fold--two { left: 796px; }

  .leaf-wash { position: absolute; background: radial-gradient(ellipse at center, rgba(217,223,182,.55), rgba(217,223,182,0) 70%); }
  .photo { position: absolute; }

  .script-heading { position: absolute; font-family: "Yesteryear", cursive; color: var(--heading); font-size: 48px; font-weight: 400; line-height: 1; white-space: nowrap; }

  .product { position: absolute; left: 40px; width: 330px; }
  .product__bottle { position: absolute; left: 6px; top: -6px; width: 40px; height: 86px; border-radius: 5px 5px 3px 3px; background: linear-gradient(180deg, #1e1a18 0 24%, #4a3524 24% 100%); }
  .product__text { margin-left: 74px; width: 236px; }
  .product__name, .plan__name { font-family: "Montserrat", sans-serif; font-weight: 600; font-size: 12.5px; color: var(--title); margin-bottom: 5px; white-space: nowrap; }
  .product__desc, .plan__desc { font-size: 13px; line-height: 17.5px; }
  .product__size, .plan__fee { font-weight: 700; font-size: 13px; margin-top: 5px; }
  .plan__fee { margin: 0 0 6px; }

  .brand { position: absolute; display: flex; flex-direction: column; align-items: center; font-family: "Libre Baskerville", serif; color: var(--logo-tone); letter-spacing: 2px; }
  .brand__mark { border-radius: 50%; background: var(--logo-tone); opacity: .55; }
  .brand--small { left: 512px; top: 24px; width: 170px; font-size: 22px; gap: 8px; }
  .brand--small .brand__mark { width: 36px; height: 36px; }
  .brand--large { left: 880px; top: 40px; width: 240px; font-size: 34px; gap: 12px; }
  .brand--large .brand__mark { width: 56px; height: 56px; }

  .plan { position: absolute; left: 424px; width: 340px; }
  .plan__text { margin-left: 33px; width: 150px; }
  .plan__text .plan__fee, .plan__text .plan__desc { padding-left: 3px; }
  .plan__photo { position: absolute; left: 201px; top: -6px; width: 133px; height: 95px; }

  .pearl { position: absolute; width: 21px; height: 21px; border-radius: 50%; background: radial-gradient(circle at 35% 35%, var(--pearl-light), var(--pearl-dark) 75%); }

  .band { position: absolute; left: 0; top: 629px; width: 1200px; height: 220px; background: var(--brown); }

  .contact { position: absolute; left: 430px; top: 644px; width: 360px; font-size: 12.5px; line-height: 15.5px; color: var(--white); }
  .contact__title { font-family: "Yesteryear", cursive; font-size: 22px; font-weight: 400; margin-bottom: 12px; }
  .contact__cols { display: flex; gap: 28px; }
  .contact__col:first-child { width: 170px; }
  .contact__label { font-weight: 700; font-size: 13px; }
  .contact__group { margin-bottom: 8px; }

  .tagline { position: absolute; left: 810px; top: 688px; width: 380px; text-align: center; font-family: "Libre Baskerville", serif; font-size: 17px; line-height: 26px; color: var(--white); }
  .badge { position: absolute; top: 772px; width: 46px; height: 46px; border-radius: 50%; }
  .badge--made { left: 942px; background: #e9d27a; border-radius: 6px; }
  .badge--organic { left: 1004px; border: 2px solid var(--cream); }
</style>
</head>
<body>
<main class="brochure">

  <div class="leaf-wash" role="img" aria-label="Soft green leaf and vine decoration" style="left:-40px;top:420px;width:460px;height:220px;"></div>
  <div class="photo" role="img" aria-label="Photo of essential oil bottles with dried herbs" style="left:178px;top:0;width:185px;height:125px;background:linear-gradient(135deg,#b8896c,#7a4a2a 55%,#c9a57f);"></div>
  <h2 class="script-heading" style="left:36px;top:136px;">Essential oils</h2>

  <article class="product" style="top:224px;">
    <div class="product__bottle" role="img" aria-label="Essential oil bottle"></div>
    <div class="product__text">
      <h3 class="product__name">Certified Organic Clementine</h3>
      <p class="product__desc">Clementine essential oil has been known to be helpful for anxiety, nervous tension and restlessness.</p>
      <p class="product__size">Size: 15ml</p>
    </div>
  </article>

  <article class="product" style="top:347px;">
    <div class="product__bottle" role="img" aria-label="Essential oil bottle"></div>
    <div class="product__text">
      <h3 class="product__name">Certified Organic Lemongrass</h3>
      <p class="product__desc">Lemongrass oil has been known to tightens the elastin fibers in the epidermis and has traditionally been used as part of a treatment for sports injuries, such as sprains and bruises.</p>
      <p class="product__size">Size: 15ml</p>
    </div>
  </article>

  <article class="product" style="top:490px;">
    <div class="product__bottle" role="img" aria-label="Essential oil bottle"></div>
    <div class="product__text">
      <h3 class="product__name">Certified Peppermint Premium</h3>
      <p class="product__desc">Peppermint has traditionally been used for its analgesic properties and has been known to be beneficial in relieving muscular aches and pains.</p>
      <p class="product__size">Size: 15ml</p>
    </div>
  </article>

  <div class="brand brand--small"><span class="brand__mark"></span><span>VEXMIRA</span></div>
  <h2 class="script-heading" style="left:456px;top:136px;">Our memberships</h2>

  <article class="plan" style="top:224px;">
    <span class="pearl" style="left:0;top:-4px;"></span>
    <div class="plan__text">
      <h3 class="plan__name">Loyalty Club Membership</h3>
      <p class="plan__fee">Annual Fee: $590</p>
      <p class="plan__desc">Loyal club members enjoy discounts and free access to facilities.</p>
    </div>
    <div class="photo plan__photo" role="img" aria-label="Photo of a makeup application" style="background:linear-gradient(135deg,#f1e6e2,#c99c8c 60%,#7a6a8a);"></div>
  </article>

  <article class="plan" style="top:355px;">
    <span class="pearl" style="left:0;top:-4px;"></span>
    <div class="plan__text">
      <h3 class="plan__name">Gold Plus</h3>
      <p class="plan__fee">Annual Fee: $590</p>
      <p class="plan__desc">Loyal club members enjoy discounts and free access to facilities.</p>
    </div>
    <div class="photo plan__photo" role="img" aria-label="Photo of a beauty treatment in a salon" style="background:linear-gradient(135deg,#8fb48a,#eef0ec 45%,#d9dde0);"></div>
  </article>

  <article class="plan" style="top:486px;">
    <span class="pearl" style="left:0;top:-4px;"></span>
    <div class="plan__text">
      <h3 class="plan__name">Platinum</h3>
      <p class="plan__fee">Annual Fee: 1950</p>
      <p class="plan__desc">Platinum members enjoy discounts and free access to facilities.</p>
    </div>
    <div class="photo plan__photo" role="img" aria-label="Photo of two friends sharing afternoon tea" style="background:linear-gradient(135deg,#d9c9a8,#e8b8a8 45%,#8aa8c8);"></div>
  </article>

  <div class="brand brand--large"><span class="brand__mark"></span><span>VEXMIRA</span></div>
  <div class="photo" role="img" aria-label="Photo of two women enjoying afternoon tea outdoors" style="left:797px;top:211px;width:403px;height:418px;background:linear-gradient(120deg,#c9b8a0,#e8c8b8 35%,#f3e8dc 55%,#9ab0c8 85%);"></div>

  <section class="band">
    <div class="leaf-wash" role="img" aria-label="Olive leaf and vine decoration" style="left:0;top:0;width:390px;height:220px;background:radial-gradient(ellipse at 40% 60%,rgba(160,130,70,.5),rgba(160,130,70,0) 70%);"></div>
    <div class="leaf-wash" role="img" aria-label="Olive leaf decoration" style="left:690px;top:20px;width:110px;height:190px;background:radial-gradient(ellipse at center,rgba(160,130,70,.35),rgba(160,130,70,0) 70%);"></div>
  </section>

  <span class="pearl" style="left:183px;top:647px;"></span>
  <span class="pearl" style="left:583px;top:647px;"></span>
  <span class="pearl" style="left:988px;top:647px;"></span>

  <section class="contact">
    <h2 class="contact__title">Contact us</h2>
    <div class="contact__cols">
      <div class="contact__col">
        <div class="contact__group">
          <p class="contact__label">Address:</p>
          <p>Level 4b,<br>27 Tarrow Lane, Brisbane,<br>Queensland 4000, Australia</p>
        </div>
        <p class="contact__group">General: enquiry@vexmira.example</p>
        <p class="contact__group">Order: order@vexmira.example</p>
      </div>
      <div class="contact__col">
        <div class="contact__group">
          <p class="contact__label">Phone:</p>
          <p>07 3000 1426</p>
        </div>
        <p class="contact__label">Our timings:</p>
        <p class="contact__group">Monday to Friday:<br>8:00 am to 12:00 pm</p>
        <p>Saturday &amp; Sunday:<br>8:00 am to 10:00 pm</p>
      </div>
    </div>
  </section>

  <p class="tagline">Certified organic skin, hair and personal<br>care products for everyone</p>
  <span class="badge badge--made" role="img" aria-label="Dunbrook crafted badge"></span>
  <span class="badge badge--organic" role="img" aria-label="Certified organic badge"></span>

  <div class="fold fold--one"></div>
  <div class="fold fold--two"></div>
</main>
</body>
</html>
```